Property Development Business Cards

I need a business card design for Tallow Creek Developments Pty Ltd. We are a property development company in Australia and our name defines the five values that we adhere to, being Profitable, Partnerships, Quality Developments, Eco Friendly and Enduring Design.

I have attached the current logo that I use, it is just five yellow circles connected to a single cricle in the middle.

Target Market(s)

Our Target audience is real estate agents, owners of properties, builders and other trades

Industry/Entity Type

Business

Requirements
Must have
• Want to have two sides to the card, one with details and one to just highlight the company

```html
<!DOCTYPE html>
<html lang="en">
<head>
<meta charset="utf-8">
<title>Tallow Creek Developments – Business Card</title>
<link rel="stylesheet" href="https://fonts.googleapis.com/css2?family=Arimo:wght@400;700&family=Roboto+Condensed:wght@400;700&family=Open+Sans+Condensed:wght@700&display=swap">
<style>
  :root {
    --stage: #141414;
    --navy-deep: #07183a;
    --navy-mid: #0b3f7a;
    --navy-ink: #0a1a8c;
    --sun: #ffc000;
    --sun-light: #ffe14a;
    --paper: #ffffff;
    --ink: #1b1b1b;
    --url-grey: #a9a9a9;
    --url-strong: #8a8a8a;
  }
  * { box-sizing: border-box; margin: 0; padding: 0; }
  html, body {
    width: 1200px; height: 720px; overflow: hidden;
    background: var(--stage);
  }
  .sheet {
    position: relative; width: 1200px; height: 720px;
    display: flex; align-items: center; justify-content: center; gap: 40px;
  }
  .card {
    position: relative; width: 538px; height: 298px;
    border-radius: 12px; overflow: hidden;
  }

  /* Front: company highlight */
  .card--front {
    background: radial-gradient(ellipse at 35% 40%, var(--navy-mid) 0%, var(--navy-deep) 75%);
  }
  .front-brand {
    position: absolute; left: 34px; top: 92px;
    font-family: "Arimo", Arial, sans-serif; font-weight: 700;
    color: var(--paper); letter-spacing: -2px;
  }
  .front-brand__name { display: block; font-size: 70px; line-height: 1; }
  .front-brand__suffix {
    display: block; font-size: 22px; letter-spacing: -0.5px;
    margin: 8px 0 0 90px;
  }
  .front-dot {
    position: absolute; right: 46px; top: 104px;
    width: 40px; height: 40px; border-radius: 50%;
    background: radial-gradient(circle at 35% 30%, var(--sun-light), var(--sun));
  }

  /* Back: details */
  .card--back { background: var(--paper); }
  .top-band {
    position: absolute; left: 0; top: 0; width: 100%; height: 36px;
    background: linear-gradient(180deg, var(--sun-light) 0%, rgba(255,224,74,0) 100%);
  }
  .back-brand {
    position: absolute; left: 30px; top: 72px; width: 230px;
    text-align: center;
    font-family: "Arimo", Arial, sans-serif; font-weight: 700;
    color: var(--navy-ink); letter-spacing: -0.5px;
  }
  .back-brand__dot {
    display: block; width: 54px; height: 54px; margin: 0 auto 18px;
    border-radius: 50%;
    background: radial-gradient(circle at 35% 30%, var(--sun-light), var(--sun));
  }
  .back-brand__name { display: block; font-size: 27px; line-height: 1; }
  .back-brand__suffix { display: block; font-size: 16px; margin-top: 3px; }

  .contact {
    position: absolute; left: 288px; top: 118px; width: 224px;
    font-family: "Roboto Condensed", Arial Narrow, sans-serif;
    color: var(--ink); font-size: 13.5px; line-height: 1.35;
  }
  .contact__name {
    font-family: "Open Sans Condensed", "Roboto Condensed", sans-serif;
    font-weight: 700; font-size: 20px; color: var(--navy-ink);
    border-bottom: 1px solid var(--ink); padding-bottom: 1px; margin-bottom: 3px;
  }
  .contact__mobile { margin-bottom: 8px; }
  .contact__mobile strong { font-weight: 700; }
  .web {
    position: absolute; left: 0; bottom: 30px; width: 100%;
    text-align: center;
    font-family: "Arimo", Arial, sans-serif; font-size: 17px;
    color: var(--url-grey); letter-spacing: -0.5px;
  }
  .web strong { color: var(--url-strong); font-weight: 700; font-size: 20px; }
</style>
</head>
<body>
<main class="sheet">
  <section class="card card--front" aria-label="Card front">
    <h1 class="front-brand">
      <span class="front-brand__name">Tallow Creek</span>
      <span class="front-brand__suffix">Developments Pty Ltd</span>
    </h1>
  </section>

  <section class="card card--back" aria-label="Card back">
    <div class="top-band" role="img" aria-label="Decorative band of yellow dots along the top edge"></div>
    <div class="back-brand">
      <span class="back-brand__dot"></span>
      <span class="back-brand__name">Tallow Creek</span>
      <span class="back-brand__suffix">Developments Pty Ltd</span>
    </div>
    <address class="contact" style="font-style:normal">
      <div class="contact__name">Daniel Mercer</div>
      <div class="contact__mobile">Mobile: <strong>0412 583 916</strong></div>
      <div>PO Box 218, Fyshwick, ACT 2609</div>
      <div>daniel@tallowcreekdevelopments.com.au</div>
    </address>
    <div class="web">www.<strong>tallowcreekdevelopments</strong>.com.au</div>
  </section>
</main>
</body>
</html>
```